Cleaning services Business Card Design

I need a business card design for my Cleaning business. I would like perhaps emphasis on the company name, Muddle to Marvel. Maybe the Muddle would to dirty and the marvel would have sprinkles.

Industry/Entity Type

Business

Contact Information for Business Card

Muddle to Marvel Cleaning Services, Tomas Ordell, Industrial, Commercial, & Residential 415-806-2147

```html
<!DOCTYPE html>
<html lang="en">
<head>
<meta charset="utf-8">
<title>Muddle to Marvel Cleaning Services – Business Card</title>
<link rel="stylesheet" href="https://fonts.googleapis.com/css2?family=PT+Sans:ital,wght@0,400;0,700;1,400&display=swap">
<style>
  :root {
    --backdrop: #3b3b3b;
    --card-white: #ffffff;
    --brand-blue: #1a9cf5;
    --brand-blue-deep: #0a86e6;
    --ink: #1c1c1c;
    --ink-soft: #6d6d6d;
    --night: #050505;
    --night-sweep: #1b1b1b;
    --silver: #c9c9c9;
    --text-light: #ffffff;
  }
  * { margin: 0; padding: 0; box-sizing: border-box; }
  html, body {
    width: 1105px; height: 1200px; overflow: hidden;
    background: var(--backdrop);
    font-family: "PT Sans", sans-serif;
  }
  .card {
    position: absolute;
    left: 196px;
    width: 720px;
    height: 410px;
    overflow: hidden;
  }
  .card--front { top: 146px; background: var(--card-white); }
  .card--back { top: 602px; background: var(--night); }

  .card__art { position: absolute; inset: 0; width: 100%; height: 100%; }

  .wordmark {
    position: absolute;
    left: 0; right: 0;
    text-align: center;
    font-weight: 700;
    text-transform: uppercase;
  }
  .wordmark__name {
    display: block;
    font-size: 56px;
    line-height: 1;
    letter-spacing: 0.01em;
  }
  .wordmark__sub {
    display: block;
    margin-top: 8px;
    font-size: 19px;
    letter-spacing: 0.58em;
    padding-left: 0.58em;
  }
  .card--front .wordmark { top: 96px; color: var(--ink); }
  .card--back .wordmark { top: 168px; color: var(--silver); }

  .holder {
    position: absolute;
    right: 426px;
    top: 296px;
    text-align: right;
    color: var(--text-light);
  }
  .holder__name { font-size: 27px; font-weight: 700; line-height: 1.1; }
  .holder__role { font-size: 20px; line-height: 1.3; }

  .divider {
    position: absolute;
    left: 322px; top: 293px;
    width: 1px; height: 70px;
    background: rgba(255,255,255,0.85);
  }

  .contacts {
    position: absolute;
    left: 350px; top: 287px;
    list-style: none;
    color: var(--text-light);
    font-size: 19.5px;
    line-height: 27px;
  }
  .contacts__item { display: flex; align-items: center; gap: 11px; }
  .contacts__icon { width: 18px; height: 18px; flex: none; }

  .services {
    position: absolute;
    left: 0; right: 0; top: 341px;
    text-align: center;
    color: var(--text-light);
    font-style: italic;
    font-size: 20px;
  }
  .services__dot {
    display: inline-block;
    width: 5px; height: 5px;
    border-radius: 50%;
    background: var(--brand-blue);
    vertical-align: middle;
    margin: 0 4px;
  }
</style>
</head>
<body>

<section class="card card--front" aria-label="Business card front">
  <svg class="card__art" viewBox="0 0 720 410" preserveAspectRatio="none" aria-hidden="true">
    <defs>
      <linearGradient id="band-blue" x1="0" y1="0" x2="1" y2="1">
        <stop offset="0" stop-color="#1c9ff7"/>
        <stop offset="0.7" stop-color="#1597f2"/>
        <stop offset="1" stop-color="#3fb0fa"/>
      </linearGradient>
    </defs>
    <path d="M0 212 Q360 276 720 222 L720 410 L0 410 Z" fill="url(#band-blue)"/>
    <path d="M0 201 Q360 264 720 211 L720 216 Q360 272 0 214 Z" fill="#111"/>
  </svg>

  <h1 class="wordmark">
    <span class="wordmark__name">Muddle to Marvel</span>
    <span class="wordmark__sub">Cleaning Services</span>
  </h1>

  <div class="holder">
    <p class="holder__name">TOMAS ORDELL</p>
    <p class="holder__role">CEO/Founder</p>
  </div>

  <div class="divider"></div>

  <ul class="contacts">
    <li class="contacts__item">
      <svg class="contacts__icon" viewBox="0 0 24 24" aria-hidden="true"><path fill="#fff" d="M6.6 10.8a15.1 15.1 0 0 0 6.6 6.6l2.2-2.2a1 1 0 0 1 1-.25 11.4 11.4 0 0 0 3.6.57 1 1 0 0 1 1 1V20a1 1 0 0 1-1 1A17 17 0 0 1 3 4a1 1 0 0 1 1-1h3.5a1 1 0 0 1 1 1c0 1.25.2 2.45.57 3.57a1 1 0 0 1-.25 1Z"/></svg>
      <span>415-806-2147</span>
    </li>
    <li class="contacts__item">
      <svg class="contacts__icon" viewBox="0 0 24 24" aria-hidden="true"><rect x="3" y="6" width="18" height="12" rx="1" fill="#fff"/><path d="M3.5 6.5 12 13l8.5-6.5" stroke="#1a9cf5" stroke-width="1.6" fill="none"/></svg>
      <span>name@cardsample.com</span>
    </li>
    <li class="contacts__item">
      <svg class="contacts__icon" viewBox="0 0 24 24" aria-hidden="true"><circle cx="12" cy="12" r="9" fill="#fff"/><path d="M3 12h18M12 3c3 3 3 15 0 18M12 3c-3 3-3 15 0 18" stroke="#1a9cf5" stroke-width="1.4" fill="none"/></svg>
      <span>www.cardsample.com</span>
    </li>
  </ul>
</section>

<section class="card card--back" aria-label="Business card back">
  <svg class="card__art" viewBox="0 0 720 410" preserveAspectRatio="none" role="img" aria-label="Dark backdrop with a diagonal light sweep and scattered faint blue sparkles">
    <defs>
      <linearGradient id="night-sweep" x1="0" y1="1" x2="1" y2="0">
        <stop offset="0" stop-color="#050505"/>
        <stop offset="0.45" stop-color="#070707"/>
        <stop offset="0.55" stop-color="#1e1e1e"/>
        <stop offset="1" stop-color="#0a0a0a"/>
      </linearGradient>
    </defs>
    <rect width="720" height="410" fill="url(#night-sweep)"/>
  </svg>

  <h2 class="wordmark">
    <span class="wordmark__name">Muddle to Marvel</span>
    <span class="wordmark__sub">Cleaning Services</span>
  </h2>

  <p class="services">Industrial<span class="services__dot"></span>Commercial<span class="services__dot"></span>Residential</p>
</section>

</body>
</html>
```